business card for larch cove dental arts
Larch Cove Dental Arts
Professional
Rowland K. Bevacquist DDS
4 Mossbank Ln
Larch Cove, NY 14093
larchcovedentalarts@mailvane.example
larchcovedentalarts.example
On the card either at the bottom or the top I would like it to say "Implants Family Dentistry Cosmetic Dentistry" to tell people what i offer, or as a motto
________ ______ has an appointment
___/___/___@ ___:___am/pm
Mon Tues Wed Thurs Fri Sat
Logo design
the white may be easier to work with for the card

```html
<!DOCTYPE html>
<html lang="en">
<head>
<meta charset="utf-8">
<title>Larch Cove Dental Arts – Business Card</title>
<link href="https://fonts.googleapis.com/css2?family=Open+Sans:wght@400;600&display=swap" rel="stylesheet">
<style>
  :root {
    --page-bg: #ececec;
    --card-light: #bfe6ea;
    --card-dark: #2f2d31;
    --accent-purple: #6f5fae;
    --ink: #2a2a2e;
    --ink-soft: #3d3d42;
    --icon-bg: #3a383d;
    --logo-ink: #ffffff;
  }
  * { margin: 0; padding: 0; box-sizing: border-box; }
  html, body {
    width: 1200px; height: 914px; overflow: hidden;
    background: var(--page-bg);
    font-family: "Open Sans", Arial, sans-serif;
  }
  .card {
    position: absolute; left: 75px; top: 157px;
    width: 1050px; height: 600px;
    background: var(--card-light);
    overflow: hidden;
    box-shadow: 0 6px 18px rgba(0,0,0,0.18);
  }
  .card-shape { position: absolute; inset: 0; }
  .doctor-name {
    position: absolute; left: 86px; top: 70px;
    font-size: 21px; font-weight: 600; color: var(--ink);
  }
  .contact-list {
    position: absolute; left: 60px; top: 300px;
    list-style: none;
  }
  .contact-item {
    display: flex; align-items: center; gap: 12px;
    height: 30px;
    font-size: 17px; color: var(--ink-soft);
  }
  .contact-item.no-icon { padding-left: 34px; }
  .contact-icon {
    width: 22px; height: 22px; border-radius: 50%;
    background: var(--icon-bg);
    display: flex; align-items: center; justify-content: center;
    flex: none;
  }
  .brand {
    position: absolute; left: 640px; top: 240px;
    display: flex; align-items: center; gap: 22px;
  }
  .brand-dot {
    width: 100px; height: 100px; border-radius: 50%;
    border: 3px solid var(--logo-ink);
    flex: none;
  }
  .brand-name {
    color: var(--logo-ink);
    font-size: 40px; font-weight: 600; line-height: 1.1;
    letter-spacing: 1px;
  }
</style>
</head>
<body>
  <div class="card">
    <svg class="card-shape" width="1050" height="600" viewBox="0 0 1050 600">
      <path d="M 650 0 C 560 50, 570 250, 490 410 C 450 490, 400 560, 370 600"
            fill="none" stroke="var(--accent-purple)" stroke-width="14"/>
      <path d="M 664 0 C 574 50, 584 250, 504 410 C 464 490, 414 560, 384 600 L 1050 600 L 1050 0 Z"
            fill="var(--card-dark)"/>
    </svg>

    <p class="doctor-name">Rowland K. Bevacquist DDS</p>

    <ul class="contact-list">
      <li class="contact-item">
        <span class="contact-icon">
          <svg width="12" height="14" viewBox="0 0 12 14"><path d="M6 0a5 5 0 0 0-5 5c0 4 5 9 5 9s5-5 5-9a5 5 0 0 0-5-5zm0 7a2 2 0 1 1 0-4 2 2 0 0 1 0 4z" fill="#fff"/></svg>
        </span>4 Mossbank Ln
      </li>
      <li class="contact-item no-icon">Larch Cove, NY 14093</li>
      <li class="contact-item">
        <span class="contact-icon">
          <svg width="12" height="12" viewBox="0 0 12 12"><path d="M2.5 0.5l2 2.5-1.2 1.5a7 7 0 0 0 4.2 4.2L9 7.5l2.5 2-1 2C5 11.5.5 7 .5 1.5z" fill="#fff"/></svg>
        </span>845-555-0172
      </li>
      <li class="contact-item">
        <span class="contact-icon">
          <svg width="12" height="10" viewBox="0 0 12 10"><rect x="0.5" y="0.5" width="11" height="9" fill="none" stroke="#fff"/><path d="M0.5 0.5L6 5.5 11.5 0.5" fill="none" stroke="#fff"/></svg>
        </span>larchcovedentalarts@mailvane.example
      </li>
      <li class="contact-item">
        <span class="contact-icon">
          <svg width="12" height="12" viewBox="0 0 12 12"><circle cx="6" cy="6" r="5.3" fill="none" stroke="#fff"/><ellipse cx="6" cy="6" rx="2.3" ry="5.3" fill="none" stroke="#fff"/><path d="M0.7 6h10.6" stroke="#fff"/></svg>
        </span>www.larchcovedentalarts.example
      </li>
    </ul>

    <div class="brand">
      <span class="brand-dot"></span>
      <p class="brand-name">Larch Cove<br>Dental Arts</p>
    </div>
  </div>
</body>
</html>
```